New flyer design for construction company marketing and description of services.

I want to have a flyer design that my techs will carry to deliver after job completion or for marketing purposes, to explain what services we provide, we offer General construction services.

Brellor Homecraft Sevices originated from a family-owned and operated contractor business, performing home renovation, addition, and construction work in the NYC area since 2004.

Today, we specialize in reliable and affordable Construction services for residential and commercial clients In 2014, we expanded to northern New Jersey. In 2016, we brought quality home improvement and repair services to new Bucks County, PA, and nearby New Jersey areas.
We offer carpentry, electrical, plumbing, renovation, remodel, cleaning services and landscaping.
I would like to have a section for home rental maintenance.

Target Market(s)

Homeowners, rental properties, real state and Senior citizen

Industry/Entity Type

Construction Company

Colors

Designer to choose colors to be used in the design.

Requirements
Must have
• A special design that will attract 55 + clients maybe a logo version that will be more attractive to seniors. I would updated the briefing with design and previous pictures, but we have all available in our social media instagram and facebook:
• https://www.pictogram.example/brellorhomecraft/?hl=en
• https://www.friendsbook.example/brellorhome/
Nice to have
• New design ideas and layouts.

```html
<!DOCTYPE html>
<html lang="en">
<head>
<meta charset="UTF-8">
<title>Brellor Homecraft Sevices – Flyer</title>
<link rel="stylesheet" href="https://fonts.googleapis.com/css2?family=Outfit:wght@200;400;600;700;800&family=Caveat:wght@500&family=Roboto:wght@400;700&display=swap">
<style>
  :root {
    --backdrop: #e8e6e3;
    --ink: #141414;
    --dark: #161616;
    --yellow: #f0c92c;
    --red: #c8102e;
    --white: #ffffff;
    --paper-light: #ffffff;
    --paper-grey: #dedede;
    --rule: #8a8a8a;
  }
  * { margin: 0; padding: 0; box-sizing: border-box; }
  html, body { width: 1200px; height: 1200px; overflow: hidden; }
  body {
    background: var(--backdrop);
    position: relative;
    font-family: "Outfit", sans-serif;
    color: var(--ink);
  }
  .flyer {
    position: absolute;
    top: 224px;
    overflow: hidden;
    box-shadow: 0 2px 6px rgba(0,0,0,.25);
  }

  /* Front side */
  .flyer-front {
    left: 134px;
    width: 446px;
    height: 686px;
    background: var(--dark);
  }
  .front-headline {
    position: absolute;
    top: 44px;
    left: 0;
    width: 100%;
    text-align: center;
    font-weight: 800;
    font-size: 76px;
    line-height: 61px;
    letter-spacing: -1px;
    color: var(--white);
    text-transform: uppercase;
    white-space: nowrap;
  }
  .front-headline .accent { color: var(--yellow); }
  .tools-visual {
    position: absolute;
    left: 10px;
    right: 0;
    top: 300px;
    bottom: 0;
    background:
      radial-gradient(ellipse at 45% 40%, rgba(240,201,44,.18), transparent 45%),
      radial-gradient(ellipse at 20% 80%, rgba(214,90,30,.22), transparent 40%),
      radial-gradient(ellipse at 70% 85%, rgba(120,120,130,.25), transparent 45%),
      linear-gradient(180deg, #1c1c1c, #121212);
  }

  /* Back side */
  .flyer-back {
    left: 623px;
    width: 448px;
    height: 690px;
    background: radial-gradient(ellipse at 50% 35%, var(--paper-light) 20%, var(--paper-grey) 100%);
  }
  .top-band { position: absolute; left: 0; top: 0; }
  .top-band-title {
    position: absolute;
    top: 14px;
    left: 0;
    width: 100%;
    text-align: center;
    font-weight: 700;
    font-size: 22px;
    letter-spacing: 4.5px;
    color: var(--ink);
  }
  .slogan {
    position: absolute;
    top: 80px;
    right: 46px;
    text-align: right;
    white-space: nowrap;
  }
  .slogan-main {
    font-weight: 800;
    font-size: 50px;
    line-height: 52px;
    letter-spacing: -1px;
  }
  .slogan-main .accent { color: var(--red); }
  .slogan-sub {
    font-weight: 200;
    font-size: 36px;
    line-height: 34px;
    letter-spacing: 0;
    margin-right: 2px;
  }
  .slogan-script {
    font-family: "Caveat", cursive;
    font-size: 20px;
    color: var(--red);
    line-height: 22px;
    margin-right: 4px;
  }
  .service-list {
    position: absolute;
    top: 204px;
    left: 0;
    width: 100%;
    list-style: none;
  }
  .service {
    position: absolute;
    width: 130px;
    text-align: center;
    font-weight: 600;
    font-size: 15px;
    line-height: 16px;
    text-transform: uppercase;
    letter-spacing: -.3px;
  }
  .service svg { display: block; margin: 0 auto 12px; }
  .service-contractor { left: 42px; }
  .service-cleaning { left: 156px; }
  .service-maintenance { left: 273px; }
  .divider {
    position: absolute;
    top: 349px;
    left: 43px;
    width: 359px;
    border-top: 1px dashed var(--rule);
  }
  .work-gallery { position: absolute; left: 45px; top: 380px; }
  .about {
    position: absolute;
    left: 276px;
    top: 384px;
    width: 150px;
    font-family: "Roboto", sans-serif;
    font-size: 11px;
    line-height: 13.5px;
  }
  .about strong { display: block; margin-bottom: 13px; font-weight: 700; }
  .footer-wave { position: absolute; left: 0; top: 0; }
  .contact-phone { position: absolute; left: 0; top: 576px; }
  .contact-phone span, .contact-mail span {
    position: absolute;
    white-space: nowrap;
    color: var(--white);
  }
  .contact-phone span {
    left: 54px;
    top: 7px;
    font-weight: 700;
    font-size: 21px;
    letter-spacing: -.3px;
  }
  .contact-mail { position: absolute; left: 0; top: 619px; }
  .contact-mail span {
    left: 50px;
    top: 8px;
    font-family: "Roboto", sans-serif;
    font-weight: 700;
    font-size: 11px;
  }
  .social-links { position: absolute; left: 28px; top: 657px; display: flex; gap: 4px; }
  .social-links span {
    width: 18px; height: 18px; border-radius: 50%;
    background: var(--ink);
  }
  .brand {
    position: absolute;
    left: 256px;
    top: 590px;
    display: flex;
    align-items: center;
    gap: 8px;
  }
  .brand-dot {
    width: 40px; height: 40px; border-radius: 50%;
    background: var(--red);
  }
  .brand-name {
    font-weight: 800;
    font-size: 36px;
    letter-spacing: -1px;
    color: var(--ink);
  }
</style>
</head>
<body>

<section class="flyer flyer-front">
  <div class="tools-visual" role="img" aria-label="Overhead arrangement of tools on a dark surface: drill, yellow hard hat, hammer, paint brush, pipe wrench, paint roller, screwdriver, hacksaw, spirit level, leaf blower, tape measure, adjustable wrench and circular saw"></div>
  <h1 class="front-headline">
    What<br>Do You<br><span class="accent">Need<br>To Fix?</span>
  </h1>
</section>

<section class="flyer flyer-back">
  <svg class="top-band" width="448" height="66" viewBox="0 0 448 66">
    <path d="M0 0H448V48H248L224 65L200 48H0Z" fill="var(--yellow)"/>
  </svg>
  <div class="top-band-title">HANDYMAN SERVICES</div>

  <div class="slogan">
    <div class="slogan-main">CALL <span class="accent">THE PROS</span></div>
    <div class="slogan-sub">NOT THE CONS</div>
    <div class="slogan-script">We do it all large and small</div>
  </div>

  <ul class="service-list">
    <li class="service service-contractor">
      <svg width="70" height="70" viewBox="0 0 70 70" fill="none" stroke="var(--ink)" stroke-width="4" stroke-linejoin="round">
        <path d="M12 50C12 32 22 20 35 20C48 20 58 32 58 50"/>
        <path d="M29 21V34M41 21V34M29 21Q35 16 41 21"/>
        <rect x="6" y="50" width="58" height="8" rx="3"/>
      </svg>
      General<br>Contractor
    </li>
    <li class="service service-cleaning">
      <svg width="70" height="70" viewBox="0 0 70 70" fill="none" stroke="var(--ink)" stroke-width="4" stroke-linecap="round" stroke-linejoin="round">
        <path d="M60 4L40 44"/>
        <path d="M34 40C42 42 46 48 42 56C30 58 18 56 10 50C18 48 26 44 34 40Z"/>
        <path d="M20 52L24 48M28 55L32 50"/>
        <circle cx="50" cy="55" r="2" fill="var(--ink)"/>
        <circle cx="56" cy="62" r="2" fill="var(--ink)"/>
        <circle cx="48" cy="64" r="2" fill="var(--ink)"/>
      </svg>
      Cleaning<br>Services
    </li>
    <li class="service service-maintenance">
      <svg width="70" height="70" viewBox="0 0 70 70" fill="none" stroke="var(--ink)" stroke-width="4" stroke-linecap="round" stroke-linejoin="round">
        <path d="M12 10L22 8L54 46M22 8L20 18L50 52"/>
        <path d="M50 52L56 62L62 58L56 48L50 52"/>
        <path d="M58 8C52 6 46 12 48 18L16 50C10 48 6 54 8 60L14 56L18 60L14 64C20 66 26 60 24 56L54 24C60 26 66 20 64 14L58 18L54 14Z"/>
      </svg>
      Property<br>Maintenance
    </li>
  </ul>

  <div class="divider"></div>

  <svg class="work-gallery" width="220" height="126" viewBox="0 0 220 126" role="img" aria-label="Two hexagon photos of finished kitchen renovations with wood cabinets and stone countertops">
    <defs>
      <linearGradient id="kitchenTone" x1="0" y1="0" x2="0" y2="1">
        <stop offset="0" stop-color="#b59a7e"/>
        <stop offset=".5" stop-color="#6b4a33"/>
        <stop offset="1" stop-color="#8e7a66"/>
      </linearGradient>
      <linearGradient id="kitchenToneLight" x1="0" y1="0" x2="0" y2="1">
        <stop offset="0" stop-color="#6f6a4e"/>
        <stop offset=".5" stop-color="#b4a894"/>
        <stop offset="1" stop-color="#5b4c3e"/>
      </linearGradient>
    </defs>
    <polygon points="52,3 101,31 101,95 52,123 3,95 3,31" fill="url(#kitchenTone)" stroke="var(--white)" stroke-width="3"/>
    <polygon points="158,3 207,31 207,95 158,123 109,95 109,31" fill="url(#kitchenToneLight)" stroke="var(--white)" stroke-width="3"/>
  </svg>

  <div class="about">
    <strong>We are a better way to get your tasks done!</strong>
    Contact us for small repairs, remodeling, general contracting, thermal inspections, cleaning services and more.
  </div>

  <svg class="footer-wave" width="448" height="690" viewBox="0 0 448 690">
    <path d="M0 524Q224 564 448 524V690H0Z" fill="var(--white)"/>
  </svg>

  <div class="contact-phone">
    <svg width="203" height="42" viewBox="0 0 203 42">
      <path d="M0 0H193L203 10V42H0Z" fill="var(--red)"/>
      <path d="M22 10C20 10 18 12 19 15C21 23 27 29 35 31C38 32 40 30 40 28L40 25L35 22L32 25C28 23 26 21 24 18L27 15L24 10Z" fill="var(--white)"/>
    </svg>
    <span>(555) 014-2738</span>
  </div>

  <div class="contact-mail">
    <svg width="224" height="32" viewBox="0 0 224 32">
      <path d="M0 0H214L224 10V32H0Z" fill="var(--yellow)"/>
      <rect x="24" y="9" width="20" height="14" fill="none" stroke="var(--white)" stroke-width="2"/>
      <path d="M24 9L34 17L44 9" fill="none" stroke="var(--white)" stroke-width="2"/>
    </svg>
    <span>hello@brellorhome.example</span>
  </div>

  <div class="social-links" aria-label="Social media">
    <span></span><span></span><span></span>
  </div>

  <div class="brand">
    <span class="brand-dot"></span>
    <span class="brand-name">Brellor</span>
  </div>
</section>

</body>
</html>
```